Business Card Design Can you design a business card design? Looking for something unique and differe

Can you design a business card design? Looking for something unique and different. Can you design a business card design? Looking for something unique and different.Can you design a business card design? Looking for something unique and different.Can you design a business card design? Looking for something unique and different.Can you design a business card design? Looking for something unique and different.Can you design a business card design? Looking for something unique and different.

Industry/Entity Type

Business

Contact Information for Business Card

Can you design a business card design? Looking for something unique and different.

Font styles to use
Serif

```html
<!DOCTYPE html>
<html lang="en">
<head>
<meta charset="utf-8">
<title>Dalton Whitmore – Business Card</title>
<link rel="stylesheet" href="https://fonts.googleapis.com/css2?family=Bebas+Neue&family=Lato:wght@400;700&display=swap">
<style>
  :root {
    --paper: #dcdcdc;
    --charcoal: #414141;
    --charcoal-deep: #363636;
    --lilac: #9a7dab;
    --lilac-shade: #6f5a7c;
    --white: #ffffff;
  }
  html, body {
    margin: 0;
    padding: 0;
    width: 1200px;
    height: 720px;
    overflow: hidden;
    background: var(--paper);
  }
  .card {
    position: relative;
    width: 1200px;
    height: 720px;
    overflow: hidden;
    background: radial-gradient(circle at 35% 50%, #e4e4e4 0%, var(--paper) 70%);
    font-family: "Lato", sans-serif;
  }
  .card__backdrop {
    position: absolute;
    inset: 0;
  }
  .brand {
    position: absolute;
    left: 0;
    width: 662px;
    top: 390px;
    display: flex;
    justify-content: center;
    align-items: center;
    gap: 16px;
  }
  .brand__mark {
    width: 26px;
    height: 26px;
    background: var(--lilac);
  }
  .brand__name {
    font-family: "Lato", sans-serif;
    font-weight: 700;
    font-size: 64px;
    color: var(--lilac);
    letter-spacing: 1px;
    line-height: 1;
  }
  .person {
    position: absolute;
    right: 85px;
    top: 74px;
    text-align: right;
    color: var(--white);
  }
  .person__name {
    margin: 0;
    font-family: "Bebas Neue", sans-serif;
    font-weight: 400;
    font-size: 76px;
    line-height: 1;
    letter-spacing: 1px;
  }
  .person__title {
    margin: 4px 0 0;
    font-size: 21px;
    line-height: 1.1;
  }
  .contacts {
    position: absolute;
    left: 640px;
    top: 278px;
    margin: 0;
    padding: 0;
    list-style: none;
  }
  .contacts__item {
    display: flex;
    align-items: center;
    height: 43px;
    color: var(--white);
    font-size: 21px;
  }
  .contacts__icon {
    width: 26px;
    height: 22px;
    margin-right: 31px;
    fill: var(--white);
  }
</style>
</head>
<body>
  <div class="card">
    <svg class="card__backdrop" width="1200" height="720" viewBox="0 0 1200 720" aria-hidden="true">
      <polygon class="dark-panel" points="501,0 1200,0 1200,720 501,720 501,645 635,512 635,208 501,80" fill="var(--charcoal)"/>
      <polygon class="tab-fold" points="615,229 635,213 635,229" fill="var(--lilac-shade)"/>
      <polygon class="tab-fold" points="615,491 635,507 635,491" fill="var(--lilac-shade)"/>
      <rect class="contact-tab" x="615" y="229" width="73" height="262" rx="6" fill="var(--lilac)"/>
    </svg>

    <div class="brand">
      <span class="brand__mark"></span>
      <span class="brand__name">Remedicor</span>
    </div>

    <header class="person">
      <h1 class="person__name">Dalton Whitmore</h1>
      <p class="person__title">Pharm.D, President</p>
    </header>

    <ul class="contacts">
      <li class="contacts__item">
        <svg class="contacts__icon" viewBox="0 0 26 22" aria-label="Phone"><path d="M2 7c0-3 5-5 11-5s11 2 11 5v2h-6V7c0-1-2-1.5-5-1.5S8 6 8 7v2H2z"/><path d="M7 10h12l3 9H4z"/></svg>
        <span>+ 555-204-3816</span>
      </li>
      <li class="contacts__item">
        <svg class="contacts__icon" viewBox="0 0 26 22" aria-label="Fax"><rect x="3" y="7" width="5" height="14" rx="1"/><rect x="10" y="1" width="10" height="7"/><rect x="9" y="9" width="14" height="12" rx="1"/></svg>
        <span>+ 555-287-9042</span>
      </li>
      <li class="contacts__item">
        <svg class="contacts__icon" viewBox="0 0 26 22" aria-label="Email"><path d="M2 4h22v14H2z"/><path d="M2 4l11 9 11-9" fill="none" stroke="var(--lilac)" stroke-width="1.6"/></svg>
        <span>dalton.whitmore@mailbox.com</span>
      </li>
      <li class="contacts__item">
        <svg class="contacts__icon" viewBox="0 0 26 22" aria-label="Address"><path d="M13 1L1 11h3v10h7v-6h4v6h7V11h3z"/></svg>
        <span>Do you want an address?</span>
      </li>
    </ul>
  </div>
</body>
</html>
```